LKND - Ledgers Kept Neatly Daily

We need a business card design for a company located in Australia - accounting / tax firm.

2 sided business card - I have attached a one-sided concept that I did in MSWord :) If anything it shows that I want a striking design - bold, fresh and less reserved than your average accounting firm's card.

Rather than having all the info on the front, maybe it could just have name and logo on front?

Want to keep colours in line with logo - orange, black and white.

Happy for full colour. Will be using a matte finish.

About Us (below)
LKND does business, and more specifically accounting and taxation differently.
People require news and other media at their fingertips so why should business figures and documents be any different?
In combination with Quilo, a cloud based accounting package, we store all receipts, tax returns and special documentation with a secure online data-storage provider and provide you with your own login. We are also interested to hear if video conferencing is something you would be interested in.
Using this technology we are able to focus more on your business and less on the data entry.

Target Market(s)

Individual mum and dad clients, and Small to Medium Business

Industry/Entity Type

Accounting

Requirements
Must have
• Must be able to edit the details at a future point in time ie - phone, address, website address, name on card and slogan.

2 sided

Standard Australian business card size
Nice to have
• Rather than having all the info on the front, maybe it could just have name and logo on front?
Should not have
• Don't want "Ledgers Kept Neatly Daily" on the card

```html
<!DOCTYPE html>
<html lang="en">
<head>
<meta charset="utf-8">
<title>LKND business card – front and back</title>
<link rel="stylesheet" href="https://fonts.googleapis.com/css2?family=Source+Sans+3:wght@300;400&display=swap">
<style>
  :root {
    --stage: #2e2e30;
    --front-dark: #2a2527;
    --front-grey: #4b4a4e;
    --back-dark: #090c13;
    --orange: #e8650f;
    --orange-deep: #a8470c;
    --sun: #ffc400;
    --link-yellow: #f6c300;
    --white: #ffffff;
    --muted: #e6e6e6;
  }
  * { box-sizing: border-box; margin: 0; padding: 0; }
  html, body {
    width: 1200px; height: 900px; overflow: hidden;
    background: var(--stage);
    font-family: "Source Sans 3", Arial, sans-serif;
  }
  .stage { position: relative; width: 1200px; height: 900px; }
  .card {
    position: absolute; top: 301px; width: 514px; height: 297px;
    overflow: hidden;
    box-shadow: 0 3px 10px rgba(0,0,0,.45);
  }
  .card--front {
    left: 73px;
    background: linear-gradient(90deg, var(--front-dark) 0%, var(--front-dark) 45%, var(--front-grey) 100%);
  }
  .card--back { left: 616px; background: var(--back-dark); }
  .front-art { position: absolute; inset: 0; }
  .brand { position: absolute; color: var(--white); text-align: right; }
  .brand__name { font-weight: 300; letter-spacing: 1px; line-height: 1; }
  .brand__services { font-weight: 400; line-height: 1.2; }
  .card--front .brand { left: 30px; top: 132px; width: 120px; }
  .card--front .brand__name { font-size: 40px; text-align: left; }
  .card--front .brand__services { font-size: 14px; margin-top: 8px; }
  .website {
    position: absolute; right: 28px; bottom: 25px;
    color: var(--link-yellow); font-size: 18px; font-weight: 400;
  }
  .mark {
    position: absolute; left: 367px; top: 30px; width: 116px; height: 116px;
  }
  .card--back .brand { right: 164px; top: 72px; width: 120px; }
  .card--back .brand__name { font-size: 27px; }
  .card--back .brand__services { font-size: 9.5px; margin-top: 5px; line-height: 1.15; }
  .person { position: absolute; left: 43px; top: 150px; }
  .person__name { color: var(--orange); font-size: 23px; font-weight: 400; line-height: 1.1; }
  .person__role { color: var(--white); font-size: 16px; font-weight: 400; margin-top: 2px; }
  .contact {
    position: absolute; color: var(--white); font-size: 15px; line-height: 19px;
    list-style: none;
  }
  .contact li { display: flex; align-items: center; gap: 6px; }
  .contact--direct { left: 43px; top: 224px; }
  .contact--address { left: 290px; top: 224px; }
  .contact--address .indent { padding-left: 17px; }
  .icon { width: 11px; height: 11px; flex: none; fill: var(--orange); }
</style>
</head>
<body>
<main class="stage">

  <section class="card card--front" aria-label="Card front">
    <svg class="front-art" viewBox="0 0 514 297" aria-hidden="true">
      <defs>
        <radialGradient id="sunGlow" cx="0.4" cy="0.45" r="0.7">
          <stop offset="0" stop-color="var(--sun)"/>
          <stop offset="0.45" stop-color="#f08a0c"/>
          <stop offset="0.8" stop-color="var(--orange)"/>
          <stop offset="1" stop-color="var(--orange)"/>
        </radialGradient>
        <linearGradient id="sunShade" x1="0" y1="0" x2="0" y2="1">
          <stop offset="0.6" stop-color="var(--orange-deep)" stop-opacity="0"/>
          <stop offset="1" stop-color="#6e2f08" stop-opacity="0.75"/>
        </linearGradient>
        <linearGradient id="greyBand" x1="0" y1="0" x2="1" y2="0">
          <stop offset="0" stop-color="#333034"/>
          <stop offset="1" stop-color="#4f4e52"/>
        </linearGradient>
      </defs>
      <path d="M300 297 Q430 230 514 90 L514 297 Z" fill="url(#greyBand)"/>
      <circle cx="340" cy="5" r="210" fill="url(#sunGlow)"/>
      <circle cx="340" cy="5" r="210" fill="url(#sunShade)"/>
    </svg>
    <div class="brand">
      <p class="brand__name">LKND</p>
      <p class="brand__services">Bookkeeping<br>Accounting<br>Taxation</p>
    </div>
    <p class="website">www.lknd.com.au</p>
  </section>

  <section class="card card--back" aria-label="Card back">
    <svg class="mark" viewBox="0 0 116 116" aria-hidden="true">
      <defs>
        <radialGradient id="markGlow" cx="0.35" cy="0.3" r="0.8">
          <stop offset="0" stop-color="var(--sun)"/>
          <stop offset="0.55" stop-color="var(--orange)"/>
          <stop offset="1" stop-color="var(--orange-deep)"/>
        </radialGradient>
      </defs>
      <circle cx="58" cy="58" r="58" fill="url(#markGlow)"/>
    </svg>
    <div class="brand">
      <p class="brand__name">LKND</p>
      <p class="brand__services">Bookkeeping<br>Accounting<br>Taxation</p>
    </div>
    <div class="person">
      <p class="person__name">Nora Pell</p>
      <p class="person__role">TAX AGENT</p>
    </div>
    <ul class="contact contact--direct">
      <li>
        <svg class="icon" viewBox="0 0 12 12" aria-hidden="true"><path d="M3 0h6a1 1 0 0 1 1 1v10a1 1 0 0 1-1 1H3a1 1 0 0 1-1-1V1a1 1 0 0 1 1-1zm.5 1.5v7.5h5V1.5z"/></svg>
        0400 555 218
      </li>
      <li>
        <svg class="icon" viewBox="0 0 12 12" aria-hidden="true"><path d="M0 2.5h12v7H0z M0 2.5l6 4 6-4" stroke="var(--back-dark)" stroke-width="0.8"/></svg>
        pell@lknd.com.au
      </li>
    </ul>
    <ul class="contact contact--address">
      <li>
        <svg class="icon" viewBox="0 0 12 12" aria-hidden="true"><path d="M6 0a4 4 0 0 1 4 4c0 3-4 8-4 8S2 7 2 4a4 4 0 0 1 4-4zm0 2.4a1.6 1.6 0 1 0 0 3.2a1.6 1.6 0 0 0 0-3.2z"/></svg>
        48 Harbour Lane
      </li>
      <li class="indent">Brookvale, NSW 2100</li>
    </ul>
  </section>

</main>
</body>
</html>
```